Rin3Vox Header

I want a professional Letterhead for my law firm. I'm attaching the letterhead I currently use in Word and PDF form. I'm also attaching my logo, and an example header that I like.

```html
<!DOCTYPE html>
<html lang="en">
<head>
<meta charset="utf-8">
<title>Rin3Vox Letterhead</title>
<link rel="stylesheet" href="https://fonts.googleapis.com/css2?family=Lato:wght@300;700;900&family=Roboto:wght@300&display=swap">
<style>
  :root {
    --bg: #e4e4e4;
    --paper: #f4f4f4;
    --brand-blue: #0a62ad;
    --brand-green: #4c7f45;
    --ink: #2a2a2a;
    --text: #4a4a4a;
    --muted: #6a6a6a;
    --rule: #c9c9c9;
    --signature: #1b4fa3;
  }
  * { box-sizing: border-box; margin: 0; padding: 0; }
  html, body { width: 1200px; height: 1200px; overflow: hidden; }
  body {
    background: var(--bg);
    position: relative;
    font-family: "Lato", sans-serif;
  }
  .letterhead {
    position: absolute;
    left: 210px;
    top: 50px;
    width: 779px;
    height: 1100px;
    background: var(--paper);
    box-shadow: 0 6px 24px rgba(0,0,0,0.12);
  }
  .band { position: absolute; left: 0; right: 0; height: 8px; }
  .band--top { top: 0; background: var(--brand-blue); }
  .band--bottom { bottom: 0; background: var(--brand-green); }

  .brand {
    position: absolute;
    left: 55px;
    top: 46px;
    display: flex;
    align-items: center;
    gap: 10px;
    font-family: "Lato", sans-serif;
    font-weight: 900;
    font-size: 42px;
    letter-spacing: 0.5px;
    color: var(--ink);
  }
  .brand__mark {
    width: 16px; height: 16px;
    background: var(--brand-blue);
  }

  .contact {
    position: absolute;
    top: 42px;
    font-family: "Roboto", sans-serif;
    font-weight: 300;
    font-size: 13px;
    line-height: 15.6px;
    color: var(--muted);
  }
  .contact--lines { left: 392px; }
  .contact--lines li { list-style: none; display: flex; align-items: center; gap: 6px; }
  .contact__icon { width: 10px; height: 10px; fill: var(--brand-blue); flex: none; }
  .contact__divider {
    position: absolute;
    left: 518px; top: 42px;
    width: 1px; height: 62px;
    background: var(--rule);
  }
  .contact--office { left: 535px; }

  .letter {
    position: absolute;
    left: 83px;
    top: 258px;
    width: 613px;
    font-weight: 300;
    font-size: 12.3px;
    line-height: 18.4px;
    color: var(--text);
  }
  .letter__date { margin-bottom: 18px; }
  .letter__recipient { margin-bottom: 36px; }
  .letter__recipient strong { font-weight: 700; color: #111; }
  .letter__salutation { margin-bottom: 18px; }
  .letter__body p { text-align: justify; margin-bottom: 18px; }
  .letter__closing { margin-top: 42px; }
  .letter__signature {
    display: block;
    width: 135px;
    height: 74px;
    margin-top: 4px;
    background: linear-gradient(135deg, rgba(27,79,163,0.18), rgba(27,79,163,0.05));
    border-radius: 2px;
  }
</style>
</head>
<body>
  <main class="letterhead">
    <div class="band band--top"></div>

    <div class="brand"><span>Rin3Vox</span><span class="brand__mark"></span></div>

    <ul class="contact contact--lines">
      <li><svg class="contact__icon" viewBox="0 0 10 10"><path d="M2 0.5 L3.6 2.6 L2.8 3.6 Q4 5.9 6.4 7.2 L7.4 6.4 L9.5 8 L8.4 9.5 Q3.5 9 0.5 1.6 Z"/></svg>(800) 555-0142</li>
      <li><svg class="contact__icon" viewBox="0 0 10 10"><rect x="2.5" y="0.5" width="5" height="2.5"/><rect x="0.5" y="3.5" width="9" height="4" rx="1"/><rect x="2.5" y="6.5" width="5" height="3"/></svg>(800) 555-0187</li>
      <li><svg class="contact__icon" viewBox="0 0 10 10"><path d="M0.5 2 H9.5 V8 H0.5 Z M0.5 2 L5 5.5 L9.5 2" fill="none" stroke="#0a62ad" stroke-width="1.2"/></svg>office@rin3vox.net</li>
      <li><svg class="contact__icon" viewBox="0 0 10 10"><g fill="none" stroke="#0a62ad" stroke-width="0.9"><circle cx="5" cy="5" r="4.4"/><ellipse cx="5" cy="5" rx="2" ry="4.4"/><path d="M0.6 5 H9.4 M1.4 2.8 H8.6 M1.4 7.2 H8.6"/></g></svg>www.rin3vox.net</li>
    </ul>
    <div class="contact__divider"></div>
    <address class="contact contact--office" style="font-style: normal;">
      Dorian K. Vale III<br>
      Attorney at Law, PLLC<br>
      2480 Harlow Street Suite 300<br>
      Westbrook, Ohio 44012
    </address>

    <article class="letter">
      <p class="letter__date">01 January 2050</p>
      <p class="letter__recipient"><strong>Company (Pvt) Ltd.</strong><br>PO Box 3355 Mainville St<br>Sample City Country 3355</p>
      <p class="letter__salutation">Dear Martin Holloway,</p>
      <div class="letter__body">
        <p>Lorem ipsum dolor sit amet, consectetuer adipiscing elit, sed diam nonummy nibh euismod tincidunt ut laoreet dolore magna aliquam erat volutpat. Ut wisi enim ad minim veniam, quis nostrud exerci tation ullamcorper suscipit lobortis nisl ut aliquip ex ea commodo consequat. Duis dolore te feugait nulla facilisi. Nam liber tempor cum soluta nobis eleifend option congue nihil imperdiet doming id quod mazim placerat facer possim assum. Lorem ipsum dolor sit amet, consectetuer adipiscing elit, sed diam nonummy nibh euismod tincidunt ut laoreet dolore magna aliquam erat volutpat. Ut wisi enim ad minim veniam, quis nostrud exerci tation ullamcorper suscipit lobortis nisl ut aliquip ex ea commodo consequat.</p>
        <p>Consectetuer adipiscing elit, sed diam nonummy nibh euismod tincidunt ut laoreet dolore magna aliquam erat volutpat. Ut wisi enim ad minim veniam, quis nostrud exerci tation ullamcorper suscipit lobortis nisl ut aliquip ex ea commodo consequat. Consectetuer adipiscing elit, sed diam nonummy nibh euismod tincidunt ut laoreet dolore magna aliquam erat volutpat. Ut wisi enim ad minim veniam, quis nostrud exerci tation ullamcorper suscipit lobortis nisl ut aliquip ex ea commodo consequat.</p>
        <p>Consectetuer adipiscing elit, sed diam nonummy nibh euismod tincidunt ut laoreet dolore magna aliquam erat volutpat. Ut wisi enim ad minim veniam, quis nostrud exerci tation ullamcorper suscipit lobortis nisl ut aliquip ex ea commodo consequat. Consectetuer adipiscing elit, sed diam nonummy nibh euismod tincidunt ut laoreet dolore magna aliquam erat volutpat. Ut wisi enim ad minim veniam, quis nostrud exerci tation ullamcorper suscipit lobortis nisl ut aliquip ex ea commodo consequat.</p>
      </div>
      <p class="letter__closing">Sincerely Yours</p>
      <span class="letter__signature" role="img" aria-label="Handwritten signature of the attorney in blue ink"></span>
    </article>

    <div class="band band--bottom"></div>
  </main>
</body>
</html>
```